Business Card Design

our business is purchasing, rehabbing and flipping homes. Design a house in the palm of a hand. This card is for a new company based in Georgia. So we buy homes that have been foreclosed, short sales,abandond, old homes and vacant homes.
We help improve the communities that we work in. We would like to see designs that use a black background with green accent and other colors that blend and don't take away from the logo and other important information.

Industry/Entity Type

Business

Contact Information for Business Card

Hollow Pine Ventures
Turning Every Key Toward Home
2867 Ledgemoor Lane
Duluth GA 30096
Office: 678-555-0142
hollowpineventuresllc.example

```html
<!DOCTYPE html>
<html lang="en">
<head>
<meta charset="utf-8">
<title>Hollow Pine Ventures – Business Card</title>
<link href="https://fonts.googleapis.com/css2?family=Fira+Sans:wght@400;500;600&family=Fira+Sans+Condensed:ital,wght@1,500&display=swap" rel="stylesheet">
<style>
  :root {
    --backdrop: #d9d9d9;
    --card: #0c0c0c;
    --card-edge: #1a1a1a;
    --green: #7ed957;
    --green-deep: #3fae5a;
    --white: #ffffff;
  }
  * { margin: 0; padding: 0; box-sizing: border-box; }
  html, body {
    width: 1200px; height: 1000px; overflow: hidden;
    background: var(--backdrop);
  }
  .card {
    position: absolute; left: 100px; top: 214px;
    width: 1000px; height: 572px;
    background: linear-gradient(135deg, var(--card-edge), var(--card) 60%);
    box-shadow: 0 12px 30px rgba(0,0,0,.35);
    font-family: "Fira Sans", sans-serif;
    color: var(--white);
  }
  .brand {
    position: absolute; left: 60px; top: 250px; width: 430px;
    text-align: center;
  }
  .brand-row {
    display: flex; align-items: center; justify-content: center; gap: 14px;
  }
  .brand-dot {
    width: 34px; height: 34px; border-radius: 50%;
    background: var(--green);
  }
  .brand-name {
    font-size: 36px; font-weight: 600; color: var(--green);
    white-space: nowrap;
  }
  .brand-tagline {
    margin-top: 10px;
    font-family: "Fira Sans Condensed", sans-serif;
    font-style: italic; font-weight: 500; font-size: 24px;
    color: var(--white);
  }
  .divider {
    position: absolute; left: 500px; top: 80px;
  }
  .contact {
    position: absolute; left: 585px; top: 90px; width: 400px;
  }
  .person-name {
    font-size: 32px; font-weight: 600; color: var(--green); letter-spacing: .5px;
  }
  .person-title {
    font-size: 20px; margin-top: 2px;
  }
  .contact-group { margin-top: 34px; }
  .contact-line {
    display: flex; align-items: center; gap: 14px;
    font-size: 22px; line-height: 32px; white-space: nowrap;
  }
  .contact-line svg { flex: none; }
  .address {
    margin-top: 30px;
    font-size: 25px; line-height: 28px; color: var(--green);
  }
</style>
</head>
<body>
  <div class="card">
    <div class="brand">
      <div class="brand-row">
        <span class="brand-dot"></span>
        <span class="brand-name">Hollow Pine Ventures</span>
      </div>
      <div class="brand-tagline">Turning Every Key Toward Home</div>
    </div>

    <svg class="divider" width="60" height="420" viewBox="0 0 60 420" aria-hidden="true">
      <defs>
        <linearGradient id="dividerFade" x1="0" y1="0" x2="0" y2="1">
          <stop offset="0" stop-color="#7ed957"/>
          <stop offset="1" stop-color="#3fae5a" stop-opacity=".6"/>
        </linearGradient>
      </defs>
      <line x1="46" y1="0" x2="10" y2="420" stroke="url(#dividerFade)" stroke-width="2"/>
    </svg>

    <div class="contact">
      <div class="person-name">Maren Ostrow</div>
      <div class="person-title">Managing Director</div>

      <div class="contact-group">
        <div class="contact-line">
          <svg width="20" height="24" viewBox="0 0 20 24" aria-hidden="true">
            <rect x="4" y="1" width="12" height="22" rx="2" fill="var(--green)"/>
            <rect x="6" y="4" width="8" height="9" fill="#0c0c0c"/>
          </svg>
          <span>00801 555 019</span>
        </div>
        <div class="contact-line">
          <svg width="24" height="20" viewBox="0 0 24 20" aria-hidden="true">
            <path d="M2 7 Q12 0 22 7 L19 10 L16 8 L16 6 Q12 4 8 6 L8 8 L5 10 Z" fill="var(--green)"/>
            <rect x="5" y="11" width="14" height="8" rx="2" fill="var(--green)"/>
          </svg>
          <span>678-555-0142</span>
        </div>
      </div>

      <div class="contact-group">
        <div class="contact-line">
          <svg width="24" height="20" viewBox="0 0 24 20" aria-hidden="true">
            <rect x="1" y="3" width="22" height="15" rx="1" fill="var(--green)"/>
            <path d="M1 3 L12 12 L23 3" fill="none" stroke="#0c0c0c" stroke-width="1.8"/>
          </svg>
          <span>info@hollowpineventuresllc.example</span>
        </div>
        <div class="contact-line">
          <svg width="24" height="24" viewBox="0 0 24 24" aria-hidden="true">
            <g fill="none" stroke="var(--green)" stroke-width="1.8">
              <circle cx="12" cy="12" r="10"/>
              <ellipse cx="12" cy="12" rx="4.5" ry="10"/>
              <line x1="2" y1="12" x2="22" y2="12"/>
              <path d="M4 7 H20 M4 17 H20"/>
            </g>
          </svg>
          <span>www.hollowpineventuresllc.example</span>
        </div>
      </div>

      <div class="address">2867 Ledgemoor Lane Duluth<br>GA 30096</div>
    </div>
  </div>
</body>
</html>
```